BrivoLane Ute.

I want the full logo on one side. And the other side the card if right Ralf the logo the left half orange like the car in the logo color with Danielle R Morrow
Founder and CEO
Email symbol then dmorrow@brivolaneute.com
Www symbol. Then Brivolaneute.com
Phone symbol then 413-926-BRIV
The very bottom would like Brivo Lane Ute is a division of Harmond Vistas. LLC

```html
<!DOCTYPE html>
<html lang="en">
<head>
<meta charset="utf-8">
<title>Brivo Lane Ute – Business Cards</title>
<link href="https://fonts.googleapis.com/css2?family=Roboto:wght@400;500;700&display=swap" rel="stylesheet">
<style>
  :root {
    --stage: #9a9a9a;
    --card-black: #0b0b0b;
    --card-white: #ffffff;
    --brand-orange: #ef9322;
    --ink-dark: #1a1a1a;
    --ink-light: #ffffff;
    --ink-muted: #bdbdbd;
  }
  html, body {
    margin: 0;
    padding: 0;
    width: 1200px;
    height: 930px;
    overflow: hidden;
    background: var(--stage);
    font-family: "Roboto", Arial, sans-serif;
  }
  .canvas {
    position: relative;
    width: 1200px;
    height: 930px;
  }
  .card {
    position: absolute;
    width: 580px;
    height: 330px;
    overflow: hidden;
    box-shadow: 0 12px 28px rgba(0,0,0,0.35);
  }
  .card--back {
    left: 70px;
    top: 90px;
    background: var(--card-black);
  }
  .card--front {
    left: 550px;
    top: 500px;
    background: var(--card-white);
  }
  .card__art {
    position: absolute;
    inset: 0;
    width: 100%;
    height: 100%;
  }
  .brand {
    position: absolute;
    display: flex;
    align-items: center;
    gap: 12px;
    font-weight: 700;
    letter-spacing: 1px;
    text-transform: uppercase;
  }
  .brand__dot {
    width: 26px;
    height: 26px;
    border-radius: 50%;
    background: var(--brand-orange);
    flex: none;
  }
  .card--back .brand {
    left: 0;
    right: 0;
    top: 130px;
    justify-content: center;
    font-size: 38px;
    color: var(--ink-light);
  }
  .back__web {
    position: absolute;
    left: 0;
    right: 0;
    bottom: 40px;
    margin: 0;
    text-align: center;
    font-size: 15px;
    color: var(--ink-light);
  }
  .back__web span { color: var(--brand-orange); }
  .card--front .brand {
    left: 34px;
    top: 120px;
    font-size: 24px;
    color: var(--ink-dark);
  }
  .contact {
    position: absolute;
    right: 26px;
    top: 88px;
    text-align: right;
    color: var(--ink-light);
    font-size: 14px;
    line-height: 1.4;
  }
  .contact__name {
    color: var(--brand-orange);
    font-weight: 700;
    font-size: 18px;
    text-transform: uppercase;
    margin: 0;
  }
  .contact__role { margin: 0 0 8px; font-size: 15px; }
  .contact__address { margin: 0 0 8px; font-style: normal; }
  .contact__line {
    display: flex;
    justify-content: flex-end;
    align-items: center;
    gap: 7px;
    margin: 0;
  }
  .contact__icon {
    width: 12px;
    height: 12px;
    fill: none;
    stroke: var(--brand-orange);
    stroke-width: 1.8;
  }
  .division {
    position: absolute;
    right: 26px;
    bottom: 10px;
    margin: 0;
    font-size: 11px;
    color: var(--ink-muted);
  }
</style>
</head>
<body>
<div class="canvas">

  <section class="card card--back" aria-label="Card back">
    <div class="brand"><span class="brand__dot"></span>Brivo Lane Ute</div>
    <p class="back__web">www.<span>Brivolaneute.com</span></p>
  </section>

  <section class="card card--front" aria-label="Card front">
    <svg class="card__art" viewBox="0 0 580 330" preserveAspectRatio="none" aria-hidden="true">
      <path d="M580 22 C430 18 350 40 318 100 C292 150 290 215 250 255 C208 295 120 300 0 300 L0 330 L580 330 Z" fill="var(--card-black)"/>
      <path d="M580 22 C430 18 350 40 318 100 C292 150 290 215 250 255 C208 295 120 300 0 300" transform="translate(-6,-8)" fill="none" stroke="var(--brand-orange)" stroke-width="7"/>
      <path d="M0 281 C120 281 195 276 232 262" fill="none" stroke="var(--brand-orange)" stroke-width="2.5"/>
    </svg>

    <div class="brand"><span class="brand__dot"></span>Brivo Lane Ute</div>

    <div class="contact">
      <p class="contact__name">Danielle R Morrow</p>
      <p class="contact__role">Founder and CEO</p>
      <address class="contact__address">214b Harlow Street,<br>Millbrook, NZ, 7304</address>
      <p class="contact__line">413-926-BRIV
        <svg class="contact__icon" viewBox="0 0 12 12"><path d="M2 1.5 L4 1.5 L5 4 L3.8 5 C4.5 6.5 5.5 7.5 7 8.2 L8 7 L10.5 8 L10.5 10 C6 10.5 1.5 6 2 1.5 Z"/></svg>
      </p>
      <p class="contact__line">dmorrow@brivolaneute.com
        <svg class="contact__icon" viewBox="0 0 12 12"><rect x="1" y="2.5" width="10" height="7"/><path d="M1 2.5 L6 6.5 L11 2.5"/></svg>
      </p>
      <p class="contact__line">www.Brivolaneute.com
        <svg class="contact__icon" viewBox="0 0 12 12"><circle cx="6" cy="6" r="4.8"/><path d="M1.2 6 H10.8 M6 1.2 C3.5 4 3.5 8 6 10.8 M6 1.2 C8.5 4 8.5 8 6 10.8"/></svg>
      </p>
    </div>

    <p class="division">Brivo Lane Ute is a division of Harmond Vistas. LLC</p>
  </section>

</div>
</body>
</html>
```